Colorful Dog Trainer Business cards

I need a logo that's an illustration of my dog's head - ideally just line work. It will also include my business name (PIM TER PAWS), Positive Reinforcement Training, my name, my certifications, phone, email, and instagram. Creative card shapes are welcome! I want it to be colorful and eye catching.
Target Market(s)
dog owners in Manhattan and Jersey City
Industry/Entity Type
dog training
Contact Information for Business Card
my business name (PIM TER PAWS), Positive Reinforcement Training, my name, my certifications, phone, email, and instagram
Look and feel

```html
<!DOCTYPE html>
<html lang="en">
<head>
<meta charset="utf-8">
<title>Pim Ter Paws – Business Cards</title>
<link href="https://fonts.googleapis.com/css2?family=Bebas+Neue&family=Oswald:wght@500&display=swap" rel="stylesheet">
<style>
  :root {
    --page: #ffffff;
    --card-front: #2a1a5e;
    --facet-1: #33206f;
    --facet-2: #2f1d66;
    --facet-3: #241552;
    --panel-left: #2a1a5e;
    --panel-right: #136b75;
    --accent: #ffc83d;
    --accent-2: #ff7a66;
    --shadow: rgba(20,10,40,0.45);
  }
  * { margin: 0; padding: 0; box-sizing: border-box; }
  html, body {
    width: 1200px; height: 1200px; overflow: hidden;
    background: var(--page);
  }
  .card {
    position: absolute;
    left: 369px; width: 462px; height: 273px;
    overflow: hidden;
    box-shadow: 12px 12px 14px var(--shadow);
  }
  .card--front { top: 277px; background: var(--card-front); }
  .card--back { top: 651px; background: var(--panel-right); }

  .facets { position: absolute; inset: 0; width: 100%; height: 100%; }

  .portrait {
    position: absolute;
    border-radius: 48% 48% 44% 44%;
    background: radial-gradient(ellipse at 50% 45%, #a08c7c 0%, #6b5648 45%, #4a3a33 70%, rgba(74,58,51,0) 100%);
  }
  .glow {
    position: absolute; border-radius: 50%;
    background: radial-gradient(circle, rgba(255,200,61,0.28) 0%, rgba(255,122,102,0.12) 45%, rgba(0,0,0,0) 70%);
  }

  .brand-name, .person-name, .contact-line {
    font-family: "Bebas Neue", "Oswald", sans-serif;
    color: var(--accent);
    font-weight: 400;
    line-height: 1;
    white-space: nowrap;
  }
  .tagline, .certifications {
    font-family: "Oswald", "Arial Narrow", sans-serif;
    font-weight: 500;
    color: var(--accent-2);
    font-size: 7.5px;
    letter-spacing: 1.3px;
    line-height: 1;
    white-space: nowrap;
  }
  .certifications { color: #ffffff; font-size: 6.5px; letter-spacing: 1px; }

  /* Front */
  .lockup { position: absolute; left: 0; right: 0; text-align: center; }
  .card--front .glow { left: 116px; top: 45px; width: 230px; height: 185px; }
  .card--front .portrait { left: 168px; top: 68px; width: 126px; height: 86px; }
  .card--front .brand-name { top: 167px; font-size: 42px; }
  .card--front .tagline { top: 207px; }

  /* Back – left panel */
  .panel-left {
    position: absolute; left: 0; top: 0; width: 210px; height: 100%;
    background: var(--panel-left);
    z-index: 2;
    box-shadow: 8px 0 14px rgba(10,5,30,0.6);
  }
  .panel-left .glow { left: 18px; top: 40px; width: 175px; height: 150px; }
  .panel-left .portrait { left: 50px; top: 70px; width: 112px; height: 77px; }
  .panel-left .brand-name { top: 160px; font-size: 37px; }
  .panel-left .tagline { top: 197px; font-size: 6.5px; }

  /* Back – right panel */
  .panel-right { position: absolute; left: 210px; top: 0; right: 0; height: 100%; }
  .person-name { position: absolute; right: 36px; top: 37px; font-size: 42px; }
  .panel-right .tagline { position: absolute; right: 36px; top: 77px; }
  .panel-right .certifications { position: absolute; right: 36px; top: 90px; }

  .contact-list { list-style: none; }
  .contact-line {
    position: absolute; right: 35px;
    display: flex; align-items: center; gap: 12px;
    font-size: 17px;
  }
  .contact-line svg { width: 17px; height: 17px; flex: none; }
  .contact-line--phone { top: 134px; }
  .contact-line--mail { top: 162px; }
  .contact-line--social { top: 190px; }
  .contact-line--home { top: 221px; }
</style>
</head>
<body>

<section class="card card--front">
  <svg class="facets" viewBox="0 0 462 273" preserveAspectRatio="none" aria-hidden="true">
    <polygon points="318,0 462,0 462,273 438,273" fill="var(--facet-1)"/>
    <polygon points="0,168 338,82 462,273 0,273" fill="var(--facet-2)"/>
    <polygon points="70,180 358,273 0,273 0,190" fill="var(--facet-3)"/>
  </svg>
  <div class="glow"></div>
  <div class="portrait" role="img" aria-label="Illustrated portrait of a shaggy dog's head"></div>
  <h1 class="brand-name lockup">PIM TER PAWS</h1>
  <p class="tagline lockup">POSITIVE REINFORCEMENT TRAINING</p>
</section>

<section class="card card--back">
  <div class="panel-left">
    <div class="glow"></div>
    <div class="portrait" role="img" aria-label="Illustrated portrait of a shaggy dog's head"></div>
    <h2 class="brand-name lockup">PIM TER PAWS</h2>
    <p class="tagline lockup">POSITIVE REINFORCEMENT TRAINING</p>
  </div>

  <div class="panel-right">
    <h2 class="person-name">YOUR NAME</h2>
    <p class="tagline">POSITIVE REINFORCEMENT TRAINING</p>
    <p class="certifications">CERTIFIED POSITIVE TRAINER · PET FIRST AID</p>

    <ul class="contact-list">
      <li class="contact-line contact-line--phone">
        <span>+12 3456 789</span>
        <svg viewBox="0 0 18 18" aria-hidden="true"><rect x="4.5" y="1" width="9" height="16" rx="1" fill="none" stroke="var(--accent)" stroke-width="1.6"/><line x1="4.5" y1="14" x2="13.5" y2="14" stroke="var(--accent)" stroke-width="1.2"/></svg>
      </li>
      <li class="contact-line contact-line--mail">
        <span>COMPANY@MAIL.COM</span>
        <svg viewBox="0 0 18 18" aria-hidden="true"><rect x="0" y="4" width="18" height="11" fill="var(--accent)"/><polyline points="0,4 9,11 18,4" fill="none" stroke="var(--panel-right)" stroke-width="1.2"/></svg>
      </li>
      <li class="contact-line contact-line--social">
        <span>@YOUR.HANDLE</span>
        <svg viewBox="0 0 18 18" aria-hidden="true"><circle cx="9" cy="9" r="7.5" fill="none" stroke="var(--accent)" stroke-width="1.8"/></svg>
      </li>
      <li class="contact-line contact-line--home">
        <span>1234&nbsp; STREET, YOUR CITY 12345</span>
        <svg viewBox="0 0 18 18" aria-hidden="true"><polygon points="9,1 18,9 15.5,9 15.5,17 2.5,17 2.5,9 0,9" fill="var(--accent)"/><rect x="6.5" y="10" width="5" height="5" fill="var(--panel-right)"/><line x1="9" y1="10" x2="9" y2="15" stroke="var(--accent)" stroke-width="1"/><line x1="6.5" y1="12.5" x2="11.5" y2="12.5" stroke="var(--accent)" stroke-width="1"/></svg>
      </li>
    </ul>
  </div>
</section>

</body>
</html>
```